Winsome Luxury Flower Shop

Need a beautiful, eye catching, elegant full-service website.
INSPIRATIONS ARE;
https://www.quillmarshblooms.com

Industry/Entity Type

retail, floral, boutique

Coding

Coded - Design and coding required

Number of Pages Required

3 page

Requirements
Must have
• SEO, Coded, UX, Fully responsive mobile, tablet, desktop, Ecommerce setup with Square, payments integration (if we use squarespace). SEO optimization with keywords, tags, meta descriptions, Load speed optimization, Google my business setup.
Nice to have
• pictures, color, elegance

```html
<!DOCTYPE html>
<html lang="en">
<head>
<meta charset="utf-8">
<title>Winsome Luxury Flower Shop</title>
<link href="https://fonts.googleapis.com/css2?family=Montserrat:wght@400;500;600;700;800;900&family=Lora:wght@400;500;600&family=Playfair+Display:wght@400&display=swap" rel="stylesheet">
<style>
:root{
  --bg:#ede8e5;
  --red:#b2182b;
  --dark:#111111;
  --ink:#222222;
  --muted:#555555;
  --line:#d5cdc9;
  --white:#ffffff;
}
*{box-sizing:border-box;margin:0;padding:0}
html,body{width:1200px;height:4454px;overflow:hidden}
body{background:var(--bg);font-family:"Lora",serif;color:var(--ink);position:relative}
.abs{position:absolute}
.sans{font-family:"Montserrat",sans-serif}

.promo-bar{left:0;top:0;width:1200px;height:26px;background:var(--dark);color:var(--white);font:500 11px "Montserrat",sans-serif;text-align:center;line-height:26px}

.brand{left:130px;top:60px;width:160px;text-align:center;color:var(--red);font:600 30px "Lora",serif;letter-spacing:1px;line-height:1}
.brand small{display:block;font-size:10px;letter-spacing:2px;margin-top:6px;color:var(--dark)}
.search{left:470px;top:59px;width:260px;height:28px;border:1px solid #777;font:400 10px "Montserrat",sans-serif;color:#555;padding:8px 12px}
.search svg{position:absolute;right:10px;top:7px}
.util{font:500 11px "Montserrat",sans-serif;color:#333;top:67px;display:flex;align-items:center;gap:8px}
.cart-badge{position:absolute;right:-6px;top:-6px;width:11px;height:11px;border-radius:50%;background:var(--red);color:#fff;font-size:7px;line-height:11px;text-align:center}
.nav{top:116px;font:500 12px "Montserrat",sans-serif;color:#333}
.nav.active{color:var(--red);border-bottom:2px solid var(--red);padding-bottom:6px}

.hero{left:0;top:159px;width:1200px;height:453px;background:linear-gradient(90deg,#6f9a4a 0%,#8aaa5e 35%,#b9b07a 60%,#d7a779 80%,#c99a67 100%)}
.hero-bouquet{left:210px;top:160px;width:460px;height:450px;border-radius:50% 50% 10% 10%;background:radial-gradient(circle at 50% 40%,#e4407a 0%,#d9477a 40%,#ea7f7b 65%,rgba(234,127,123,0) 72%)}
.hero-eyebrow{left:700px;top:222px;font:800 37px "Montserrat",sans-serif;color:#fff}
.hero-title{left:698px;top:266px;font:900 88px "Montserrat",sans-serif;color:#fff;line-height:1}
.hero-sub{left:705px;top:378px;width:320px;font:700 17px/28px "Montserrat",sans-serif;color:#fff;text-transform:uppercase}
.btn-red{background:var(--red);color:#fff;font:700 13px "Montserrat",sans-serif;text-align:center;text-transform:uppercase}
.hero-btn{left:707px;top:455px;width:137px;height:38px;line-height:38px;font-size:14px}
.arrow{top:362px}

.tab{top:664px;font:700 25px "Montserrat",sans-serif;text-transform:uppercase}
.photo{position:absolute}
.card{width:273px;top:759px;height:374px}
.card.raised{background:#fff}
.card .photo{left:0;top:0;width:273px;height:297px}
.card .name{position:absolute;top:318px;width:100%;text-align:center;font-size:12px}
.card .price{position:absolute;top:337px;width:100%;text-align:center;font-size:12px}
.hover-btn{position:absolute;left:50%;transform:translateX(-50%);width:76px;height:20px;font:400 10px "Lora",serif;text-align:center;line-height:20px}
.hover-btn.view{background:rgba(255,255,255,.85);color:#444}
.hover-btn.add{background:var(--red);color:#fff}

.section-title{left:0;width:1200px;text-align:center;font:800 30px "Montserrat",sans-serif;color:var(--dark);text-transform:uppercase;display:flex;justify-content:center;align-items:center;gap:22px}
.rose{display:inline-block;width:30px;height:36px;border-radius:50% 50% 45% 45%;background:radial-gradient(circle at 50% 40%,#c0172c,#7a0f1a)}
.rule{left:582px;width:36px;height:2px;background:var(--dark)}

.pick{width:150px;text-align:center}
.pick .flourish{height:30px;border-radius:15px;background:linear-gradient(90deg,rgba(80,80,80,0),rgba(80,80,80,.35),rgba(80,80,80,0))}
.pick .label{font-size:16px;margin-top:6px}
.pick svg{display:block;margin:12px auto 0}
.pick.active .label{color:var(--red)}
.pick.active .flourish{background:linear-gradient(90deg,rgba(178,24,43,0),rgba(178,24,43,.4),rgba(178,24,43,0))}

.coll-title{left:178px;top:1528px;font:800 30px "Montserrat",sans-serif;color:var(--dark)}
.coll-sub{left:178px;top:1565px;font-size:14px;color:#333}
.outline-btn{border:1px solid var(--red);color:var(--red);font:400 12px "Lora",serif;display:flex;align-items:center;justify-content:center;gap:10px}
.circle-arrow{width:26px;height:26px;border:1.5px solid #222;border-radius:50%}

.tile{width:221px;height:310px}
.tile .photo{left:0;top:0;width:221px;height:221px}
.tile .stars{position:absolute;top:237px;left:0;color:var(--red);font-size:12px;letter-spacing:1px}
.tile .name{position:absolute;top:260px;left:0;font-size:12px}
.tile .price{position:absolute;top:278px;left:0;font-size:12px}

.banner{top:1971px;width:400px;height:355px}
.banner-text{position:absolute;left:0;width:100%;top:137px;text-align:center;font:800 32px "Montserrat",sans-serif;color:#fff}
.banner-btn{position:absolute;top:194px;left:50%;transform:translateX(-50%);width:95px;height:27px;line-height:27px;font-size:11px;border:1px solid #fff}

.testi{top:3405px;width:221px;height:278px;border:1px solid var(--line);background:var(--bg);padding:22px 24px}
.testi .q{font:700 28px "Montserrat",sans-serif;color:#9a9a9a;line-height:1}
.testi .stars{color:var(--red);font-size:11px;letter-spacing:2px;margin-top:6px}
.testi p{font:400 8.5px/13.5px "Montserrat",sans-serif;color:#444;margin-top:12px;text-align:center}
.author{display:flex;align-items:center;gap:10px;margin-top:14px;font:700 8px "Montserrat",sans-serif}
.author span{display:block;font-weight:400;margin-top:2px}
.avatar{width:24px;height:24px;border-radius:50%;background:#d9a742}
.testi.faded{opacity:.35}
.dot{top:3733px;width:6px;height:6px;border-radius:50%;background:#c9c2bf}

.promo{top:3807px;width:459px;height:279px}
.promo-title{position:absolute;font:400 40px/40px "Playfair Display",serif}
.promo-copy{position:absolute;font-size:11px;line-height:15px;width:130px}
.promo-btn{position:absolute;width:92px;height:26px;line-height:26px;font-size:10px}

.footer{left:0;top:4146px;width:1200px;height:308px;background:var(--dark);color:#fff}
.f-brand{left:130px;top:4220px;width:190px;text-align:center;font:600 34px "Lora",serif;color:#fff;line-height:1}
.f-brand small{display:block;font-size:10px;letter-spacing:2px;margin-top:8px}
.f-col{top:4191px;font:400 9.5px/19px "Montserrat",sans-serif;color:#ccc}
.f-col h4{font:700 10px "Montserrat",sans-serif;color:#fff;margin-bottom:10px;letter-spacing:.5px}
.f-email{left:813px;top:4224px;width:256px;height:29px;border:1px solid #aaa;font:400 9px "Montserrat",sans-serif;color:#ddd;padding:9px 16px}
.social{top:4284px;width:22px;height:22px;border:1px solid #fff;border-radius:50%}
.copy{left:130px;top:4383px;font:400 9px "Montserrat",sans-serif;color:#ddd}
.pay{top:4389px;width:23px;height:15px;background:#e8e8e8;border-radius:2px}
</style>
</head>
<body>

<div class="abs promo-bar">Don't Wait! Save 10% with Code BTF10</div>

<!-- Header -->
<div class="abs brand">WINSOME<small>FLOWER BOUTIQUE</small></div>
<div class="abs search">Search
  <svg width="12" height="12" viewBox="0 0 12 12"><circle cx="5" cy="5" r="4" fill="none" stroke="#333" stroke-width="1.2"/><line x1="8" y1="8" x2="11" y2="11" stroke="#333" stroke-width="1.2"/></svg>
</div>
<div class="abs util" style="left:778px">
  <svg width="26" height="16" viewBox="0 0 26 16"><rect x="1" y="2" width="15" height="10" fill="none" stroke="#333"/><path d="M16 5h5l3 4v3h-8z" fill="none" stroke="#333"/><circle cx="6" cy="13" r="2" fill="#fff" stroke="#333"/><circle cx="20" cy="13" r="2" fill="#fff" stroke="#333"/></svg>
  Free Delivery</div>
<div class="abs util" style="left:946px">Sign in
  <svg width="16" height="16" viewBox="0 0 16 16"><circle cx="8" cy="5" r="3.5" fill="none" stroke="#333"/><path d="M1.5 15c1-4 12-4 13 0" fill="none" stroke="#333"/></svg></div>
<div class="abs util" style="left:1013px">Cart
  <span style="position:relative;display:inline-block"><svg width="18" height="18" viewBox="0 0 18 18"><path d="M3 5h12l-1 11H4z" fill="none" stroke="#333" stroke-width="1.3"/><path d="M6 7V4a3 3 0 016 0v3" fill="none" stroke="#333" stroke-width="1.3"/></svg><span class="cart-badge">0</span></span></div>

<div class="abs nav active" style="left:470px">About Us</div>
<div class="abs nav" style="left:557px">Shop All</div>
<div class="abs nav" style="left:641px">Occasions</div>
<div class="abs nav" style="left:731px">Collections</div>
<div class="abs nav" style="left:830px">Flowers</div>
<div class="abs nav" style="left:909px">Best Sellers</div>
<div class="abs nav" style="left:1010px">Contact Us</div>

<!-- Hero -->
<div class="abs hero" role="img" aria-label="Pink and coral tulip bouquet in a glass vase on a garden table"></div>
<div class="abs hero-bouquet" role="img" aria-label="Tulip bouquet"></div>
<div class="abs hero-eyebrow">LUXURY IN</div>
<div class="abs hero-title">BLOOM</div>
<div class="abs hero-sub">Lorem Ipsum is simply dummy text of the printing and</div>
<div class="abs btn-red hero-btn">Shop Now</div>
<svg class="abs arrow" style="left:56px" width="26" height="50" viewBox="0 0 26 50"><path d="M22 2L4 25l18 23" fill="none" stroke="#fff" stroke-width="3"/></svg>
<svg class="abs arrow" style="left:1104px" width="26" height="50" viewBox="0 0 26 50"><path d="M4 2l18 23L4 48" fill="none" stroke="#fff" stroke-width="3"/></svg>

<!-- Best sellers -->
<div class="abs tab" style="left:408px;color:var(--red)">Best Sellers</div>
<div class="abs tab" style="left:618px;color:var(--dark)">Add Ons</div>

<div class="abs card raised" style="left:24px">
  <div class="photo" role="img" aria-label="Peach rose arrangement in a grey stone vase" style="background:linear-gradient(180deg,#c9b59c,#b9a58d 60%,#7a7a78)"></div>
  <div class="hover-btn view" style="top:107px">View Detail</div>
  <div class="hover-btn add" style="top:142px">Add To Cart</div>
  <div class="name">Lorem Ipsum is simply dum</div><div class="price">$25.99</div>
</div>
<div class="abs card" style="left:320px">
  <div class="photo" role="img" aria-label="Wrapped bouquet of tulips and greenery in kraft paper" style="background:linear-gradient(160deg,#6b4a36,#8a6b4e 50%,#5b7d3e)"></div>
  <div class="name">Lorem Ipsum is simply dum</div><div class="price">$25.99</div>
</div>
<div class="abs card" style="left:614px">
  <div class="photo" role="img" aria-label="Bright mixed bouquet in a grey bucket" style="background:linear-gradient(180deg,#3a3028,#c26a3a 40%,#8b6aa0 60%,#6f6f6f)"></div>
  <div class="name">Lorem Ipsum is simply dum</div><div class="price">$25.99</div>
</div>
<div class="abs card" style="left:906px">
  <div class="photo" role="img" aria-label="Pink peony and yellow flower arrangement in a grey pot" style="background:linear-gradient(180deg,#5a6e45,#e08a8a 45%,#d9b148 65%,#6c6c6c)"></div>
  <div class="name">Lorem Ipsum is simply dum</div><div class="price">$25.99</div>
</div>

<!-- Top picks -->
<div class="abs section-title" style="top:1190px"><span class="rose" role="img" aria-label="Red rose"></span>Top Picks<span class="rose" role="img" aria-label="Red rose"></span></div>
<div class="abs rule" style="top:1245px"></div>

<div class="abs pick" style="left:127px;top:1305px">
  <div class="flourish" role="img" aria-label="Decorative flourish"></div>
  <svg width="26" height="26" viewBox="0 0 26 26"><rect x="4" y="14" width="18" height="9" fill="none" stroke="#222" stroke-width="1.4"/><rect x="7" y="8" width="12" height="6" fill="none" stroke="#222" stroke-width="1.4"/><line x1="13" y1="3" x2="13" y2="8" stroke="#222" stroke-width="1.4"/></svg>
  <div class="label">Birthday</div>
  <div class="flourish" style="margin-top:14px" role="img" aria-label="Decorative flourish"></div>
</div>
<div class="abs pick" style="left:321px;top:1305px">
  <div class="flourish" role="img" aria-label="Decorative flourish"></div>
  <svg width="26" height="26" viewBox="0 0 26 26"><circle cx="10" cy="8" r="4" fill="none" stroke="#222" stroke-width="1.4"/><circle cx="17" cy="11" r="3" fill="none" stroke="#222" stroke-width="1.4"/><path d="M10 12l-3 12M17 14l-6 10" stroke="#222" stroke-width="1.4"/></svg>
  <div class="label">Anniversary</div>
  <div class="flourish" style="margin-top:14px" role="img" aria-label="Decorative flourish"></div>
</div>
<div class="abs pick active" style="left:521px;top:1305px">
  <div class="flourish" role="img" aria-label="Decorative flourish"></div>
  <svg width="26" height="26" viewBox="0 0 26 26"><path d="M7 4h12l-2 9H9z" fill="none" stroke="#b2182b" stroke-width="1.4"/><path d="M9 13l4 11 4-11" fill="none" stroke="#b2182b" stroke-width="1.4"/></svg>
  <div class="label">New Arrivals</div>
  <div class="flourish" style="margin-top:14px" role="img" aria-label="Decorative flourish"></div>
</div>
<div class="abs pick" style="left:719px;top:1305px">
  <div class="flourish" role="img" aria-label="Decorative flourish"></div>
  <svg width="26" height="26" viewBox="0 0 26 26"><path d="M13 22S3 15 3 9a5 5 0 0110-1 5 5 0 0110 1c0 6-10 13-10 13z" fill="none" stroke="#222" stroke-width="1.4"/></svg>
  <div class="label">Love</div>
  <div class="flourish" style="margin-top:14px" role="img" aria-label="Decorative flourish"></div>
</div>
<div class="abs pick" style="left:912px;top:1305px">
  <div class="flourish" role="img" aria-label="Decorative flourish"></div>
  <svg width="26" height="26" viewBox="0 0 26 26"><circle cx="9" cy="15" r="6" fill="none" stroke="#222" stroke-width="1.4"/><circle cx="17" cy="15" r="6" fill="none" stroke="#222" stroke-width="1.4"/></svg>
  <div class="label">Wedding</div>
  <div class="flourish" style="margin-top:14px" role="img" aria-label="Decorative flourish"></div>
</div>

<!-- Collections -->
<span class="abs rose" style="left:130px;top:1535px" role="img" aria-label="Red rose"></span>
<div class="abs coll-title">COLLECTIONS</div>
<div class="abs coll-sub">Love in Full Bloom: Celebrate Love</div>
<div class="abs outline-btn" style="left:904px;top:1539px;width:165px;height:43px">View All Collections
  <svg width="8" height="12" viewBox="0 0 8 12"><path d="M1 1l5 5-5 5" fill="none" stroke="#b2182b" stroke-width="1.5"/></svg></div>

<svg class="abs circle-arrow" style="left:65px;top:1713px" viewBox="0 0 26 26"><path d="M15 8l-5 5 5 5" fill="none" stroke="#222" stroke-width="1.5"/></svg>
<svg class="abs circle-arrow" style="left:1099px;top:1713px" viewBox="0 0 26 26"><path d="M11 8l5 5-5 5" fill="none" stroke="#222" stroke-width="1.5"/></svg>

<div class="abs tile" style="left:130px;top:1617px">
  <div class="photo" role="img" aria-label="White and burgundy flower arrangement in a white vase" style="background:linear-gradient(180deg,#4a3a30,#c9b8b0 40%,#7a1e2a 60%,#d8d2cc)"></div>
  <div class="stars">★★★★★</div><div class="name">Lorem Ipsum is simply dum</div><div class="price">$25.99</div>
</div>
<div class="abs tile" style="left:372px;top:1617px">
  <div class="photo" role="img" aria-label="Red rose arrangement in a red velvet box" style="background:linear-gradient(180deg,#3b3026,#8a1a22 45%,#a01827 75%,#5a4a3e)"></div>
  <div class="hover-btn view" style="top:80px">View Detail</div>
  <div class="hover-btn add" style="top:114px">Add To Cart</div>
  <div class="stars">★★★★★</div><div class="name">Lorem Ipsum is simply dum</div><div class="price">$25.99</div>
</div>
<div class="abs tile" style="left:610px;top:1617px">
  <div class="photo" role="img" aria-label="Orange and yellow flowers in a terracotta pot" style="background:linear-gradient(180deg,#4a2a22,#e0a040 40%,#c4704a 75%,#6a3a2a)"></div>
  <div class="stars">★★★★★</div><div class="name">Lorem Ipsum is simply dum</div><div class="price">$25.99</div>
</div>
<div class="abs tile" style="left:849px;top:1617px">
  <div class="photo" role="img" aria-label="Red and orange lily arrangement in a white bowl" style="background:linear-gradient(180deg,#4a5030,#c0242c 35%,#e66a2c 60%,#b8b8a8)"></div>
  <div class="stars">★★★★★</div><div class="name">Lorem Ipsum is simply dum</div><div class="price">$25.99</div>
</div>

<!-- Category banners -->
<div class="abs banner" style="left:0" role="img" aria-label="Round pink and white rose bouquet on a wooden table" >
  <div style="position:absolute;inset:0;background:radial-gradient(circle at 50% 50%,#e48aa8 0%,#c86a84 35%,#6a4430 70%,#4a3020 100%)"></div>
  <div class="banner-text">CLASSIC</div><div class="btn-red banner-btn">Shop Now</div>
</div>
<div class="abs banner" style="left:400px" role="img" aria-label="Pink roses in a glass bowl">
  <div style="position:absolute;inset:0;background:radial-gradient(circle at 50% 40%,#e07a98 0%,#a5607a 40%,#4a4a4a 80%,#3a3a3c 100%)"></div>
  <div class="banner-text">CRYSTAL</div><div class="btn-red banner-btn">Shop Now</div>
</div>
<div class="abs banner" style="left:800px" role="img" aria-label="Red rose and cotton arrangement in a bronze urn">
  <div style="position:absolute;inset:0;background:radial-gradient(circle at 55% 45%,#a0202c 0%,#6a3a34 40%,#3e4a3a 75%,#2e3a2e 100%)"></div>
  <div class="banner-text">PREMIUM</div><div class="btn-red banner-btn">Shop Now</div>
</div>

<!-- New flowers -->
<div class="abs section-title" style="top:2402px"><span class="rose" role="img" aria-label="Red rose"></span>New Flowers<span class="rose" role="img" aria-label="Red rose"></span></div>
<div class="abs rule" style="top:2457px"></div>

<div class="abs tile" style="left:130px;top:2512px">
  <div class="photo" role="img" aria-label="White and red flower arrangement in a shop window" style="background:linear-gradient(180deg,#3a3030,#c9bcb6 45%,#8a2030 60%,#d5d0cc)"></div>
  <div class="hover-btn view" style="top:80px">View Detail</div>
  <div class="hover-btn add" style="top:114px">Add To Cart</div>
  <div class="stars">★★★★★</div><div class="name">Lorem Ipsum is simply dum</div><div class="price">$25.99</div>
</div>
<div class="abs tile" style="left:372px;top:2512px">
  <div class="photo" role="img" aria-label="Mixed bouquet of peach roses and purple blooms" style="background:linear-gradient(180deg,#5a6a3a,#e8a890 40%,#7a3a70 60%,#6a7a4a)"></div>
  <div class="stars">★★★★★</div><div class="name">Lorem Ipsum is simply dum</div><div class="price">$25.99</div>
</div>
<div class="abs tile" style="left:610px;top:2512px">
  <div class="photo" role="img" aria-label="Pink tulip bouquet wrapped in blue paper" style="background:linear-gradient(180deg,#8a7a6a,#e8a8b4 40%,#a8bcc8 75%,#c9b4a8)"></div>
  <div class="stars">★★★★★</div><div class="name">Lorem Ipsum is simply dum</div><div class="price">$25.99</div>
</div>
<div class="abs tile" style="left:849px;top:2512px">
  <div class="photo" role="img" aria-label="Soft pastel rose arrangement in a tall vase" style="background:linear-gradient(180deg,#c9a878,#e8c0b0 40%,#8aa070 65%,#b8a890)"></div>
  <div class="stars">★★★★★</div><div class="name">Lorem Ipsum is simply dum</div><div class="price">$25.99</div>
</div>
<div class="abs tile" style="left:130px;top:2829px">
  <div class="photo" role="img" aria-label="White and burgundy flower arrangement in a white vase" style="background:linear-gradient(180deg,#4a3a30,#c9b8b0 40%,#7a1e2a 60%,#d8d2cc)"></div>
  <div class="stars">★★★★★</div><div class="name">Lorem Ipsum is simply dum</div><div class="price">$25.99</div>
</div>
<div class="abs tile" style="left:372px;top:2829px">
  <div class="photo" role="img" aria-label="Red rose arrangement in a red velvet box" style="background:linear-gradient(180deg,#3b3026,#8a1a22 45%,#a01827 75%,#5a4a3e)"></div>
  <div class="stars">★★★★★</div><div class="name">Lorem Ipsum is simply dum</div><div class="price">$25.99</div>
</div>
<div class="abs tile" style="left:610px;top:2829px">
  <div class="photo" role="img" aria-label="Orange and yellow flowers in a terracotta pot" style="background:linear-gradient(180deg,#4a2a22,#e0a040 40%,#c4704a 75%,#6a3a2a)"></div>
  <div class="stars">★★★★★</div><div class="name">Lorem Ipsum is simply dum</div><div class="price">$25.99</div>
</div>
<div class="abs tile" style="left:849px;top:2829px">
  <div class="photo" role="img" aria-label="Red and orange lily arrangement in a white bowl" style="background:linear-gradient(180deg,#4a5030,#c0242c 35%,#e66a2c 60%,#b8b8a8)"></div>
  <div class="stars">★★★★★</div><div class="name">Lorem Ipsum is simply dum</div><div class="price">$25.99</div>
</div>

<div class="abs outline-btn" style="left:550px;top:3169px;width:110px;height:45px">View All
  <svg width="8" height="12" viewBox="0 0 8 12"><path d="M1 1l5 5-5 5" fill="none" stroke="#b2182b" stroke-width="1.5"/></svg></div>

<!-- Testimonials -->
<div class="abs section-title" style="top:3292px"><span class="rose" role="img" aria-label="Red rose"></span>Testimonials<span class="rose" role="img" aria-label="Red rose"></span></div>
<div class="abs rule" style="top:3349px"></div>

<div class="abs testi faded" style="left:-107px">
  <div class="q">&ldquo;</div><div class="stars">★★★★★</div>
  <p>At vero eos et accusamus et iusto odio dignissimos ducimus qui blanditiis praesentium voluptatum deleniti atque corrupti quos dolores et quas molestias excepturi sint occaecati cupiditate non provident, similique sunt in culpa qui officia deserunt mollitia animi, id est laborum et dolorum fuga. Et harum quidem rerum facilis.</p>
  <div class="author"><div class="avatar" role="img" aria-label="Customer portrait"></div><div>DARA PENFOLD<span>2 Days Ago</span></div></div>
</div>
<div class="abs testi" style="left:133px">
  <div class="q">&ldquo;</div><div class="stars">★★★★★</div>
  <p>At vero eos et accusamus et iusto odio dignissimos ducimus qui blanditiis praesentium voluptatum deleniti atque corrupti quos dolores et quas molestias excepturi sint occaecati cupiditate non provident, similique sunt in culpa qui officia deserunt mollitia animi, id est laborum et dolorum fuga. Et harum quidem rerum facilis.</p>
  <div class="author"><div class="avatar" role="img" aria-label="Customer portrait"></div><div>DARA PENFOLD<span>2 Days Ago</span></div></div>
</div>
<div class="abs testi" style="left:372px">
  <div class="q">&ldquo;</div><div class="stars">★★★★★</div>
  <p>At vero eos et accusamus et iusto odio dignissimos ducimus qui blanditiis praesentium voluptatum deleniti atque corrupti quos dolores et quas molestias excepturi sint occaecati cupiditate non provident, similique sunt in culpa qui officia deserunt mollitia animi, id est laborum et dolorum fuga. Et harum quidem rerum facilis.</p>
  <div class="author"><div class="avatar" role="img" aria-label="Customer portrait"></div><div>DARA PENFOLD<span>2 Days Ago</span></div></div>
</div>
<div class="abs testi" style="left:610px">
  <div class="q">&ldquo;</div><div class="stars">★★★★★</div>
  <p>At vero eos et accusamus et iusto odio dignissimos ducimus qui blanditiis praesentium voluptatum deleniti atque corrupti quos dolores et quas molestias excepturi sint occaecati cupiditate non provident, similique sunt in culpa qui officia deserunt mollitia animi, id est laborum et dolorum fuga. Et harum quidem rerum facilis.</p>
  <div class="author"><div class="avatar" role="img" aria-label="Customer portrait"></div><div>DARA PENFOLD<span>2 Days Ago</span></div></div>
</div>
<div class="abs testi" style="left:849px">
  <div class="q">&ldquo;</div><div class="stars">★★★★★</div>
  <p>At vero eos et accusamus et iusto odio dignissimos ducimus qui blanditiis praesentium voluptatum deleniti atque corrupti quos dolores et quas molestias excepturi sint occaecati cupiditate non provident, similique sunt in culpa qui officia deserunt mollitia animi, id est laborum et dolorum fuga. Et harum quidem rerum facilis.</p>
  <div class="author"><div class="avatar" role="img" aria-label="Customer portrait"></div><div>DARA PENFOLD<span>2 Days Ago</span></div></div>
</div>
<div class="abs testi faded" style="left:1087px">
  <div class="q">&ldquo;</div><div class="stars">★★★★★</div>
  <p>At vero eos et accusamus et iusto odio dignissimos ducimus qui blanditiis praesentium voluptatum deleniti atque corrupti quos dolores et quas molestias excepturi sint occaecati cupiditate non provident, similique sunt in culpa qui officia deserunt mollitia animi, id est laborum et dolorum fuga. Et harum quidem rerum facilis.</p>
  <div class="author"><div class="avatar" role="img" aria-label="Customer portrait"></div><div>DARA PENFOLD<span>2 Days Ago</span></div></div>
</div>

<div class="abs dot" style="left:565px;background:var(--red)"></div>
<div class="abs dot" style="left:581px"></div>
<div class="abs dot" style="left:597px"></div>
<div class="abs dot" style="left:613px"></div>
<div class="abs dot" style="left:629px"></div>

<!-- For Her / For Him -->
<div class="abs promo" style="left:130px;background:#e6e1dc">
  <div class="photo" style="left:0;top:0;width:290px;height:279px;background:linear-gradient(120deg,#d8d2cc,#c9c0b8 50%,#d88aa8 75%,#c9c2bc)" role="img" aria-label="Florist in a white shirt holding a pink wrapped bouquet"></div>
  <div class="promo-title" style="left:299px;top:58px;color:var(--red)">For<br>Her</div>
  <div class="promo-copy" style="left:304px;top:141px;color:#333">Sed ut perspiciatis unde omnis iste natus error sit voluptatem accusantium doloremque.</div>
  <div class="btn-red promo-btn" style="left:304px;top:210px">Shop Now</div>
</div>
<div class="abs promo" style="left:609px;background:linear-gradient(90deg,#4a3a30,#2e2620)" role="img" aria-label="Florist in an apron arranging white roses in a dark shop">
  <div class="promo-title" style="left:300px;top:58px;color:#fff">For<br>Him</div>
  <div class="promo-copy" style="left:303px;top:141px;color:#eee">Sed ut perspiciatis unde omnis iste natus error sit voluptatem accusantium doloremque.</div>
  <div class="btn-red promo-btn" style="left:303px;top:210px">Shop Now</div>
</div>

<!-- Footer -->
<div class="abs footer"></div>
<div class="abs f-brand">WINSOME<small>FLOWER BOUTIQUE</small></div>
<div class="abs f-col" style="left:370px"><h4>SHOPPING</h4>Wishlist<br>Shop by Brand<br>Offers<br>Track order<br>Size Guide</div>
<div class="abs f-col" style="left:519px"><h4>INFOMATION</h4>Track Order<br>Shipping &amp; Returns<br>About us<br>Help<br>Gift Cards</div>
<div class="abs f-col" style="left:681px"><h4>ACCOUNT</h4>Cart<br>My account<br>My orders<br>Wishlist<br>Affiliate Program</div>
<div class="abs f-col" style="left:809px"><h4>LET'S KEEP IN TOUCH</h4></div>
<div class="abs f-email">Enter your email address
  <svg style="position:absolute;right:12px;top:10px" width="10" height="8" viewBox="0 0 10 8"><path d="M0 4h9M6 1l3 3-3 3" fill="none" stroke="#fff"/></svg></div>
<div class="abs social" style="left:810px"></div>
<div class="abs social" style="left:838px"></div>
<div class="abs social" style="left:866px"></div>
<div class="abs social" style="left:894px"></div>
<div class="abs copy">Copyright © 2025 All Rights Reserved</div>
<div class="abs pay" style="left:882px"></div>
<div class="abs pay" style="left:909px"></div>
<div class="abs pay" style="left:936px"></div>
<div class="abs pay" style="left:963px"></div>
<div class="abs pay" style="left:990px"></div>
<div class="abs pay" style="left:1017px"></div>
<div class="abs pay" style="left:1044px"></div>

</body>
</html>
```